Business Card for my building company

I would like the card to make a statement, so as soon as you see the card you think "wow nice card' and then read the details on the card its self. Also i would like to be able to put in the detail for the MUST HAVES so please Crete a box that i can alter depending on who in my business needs the cards. Thank you

Target Market(s)

Any one looking to build a house/ townhouse or duplex

Industry/Entity Type

Home Builder

Contact Information for Business Card

I would like the card to have the logo on the card and the must haves

Font styles to use
Sans Serif

Requirements
Must have
• Name
• Phone Number
• Email Address
• Website
• Licence Number
• Abn

```html
<!DOCTYPE html>
<html lang="en">
<head>
<meta charset="utf-8">
<title>Ridgeline Builders – Business Card</title>
<link href="https://fonts.googleapis.com/css2?family=Roboto+Condensed:wght@400;700&display=swap" rel="stylesheet">
<style>
  :root {
    --bg: #e9e6e1;
    --gold: #c9a34b;
    --ink: #111111;
    --accent-red: #8e1b16;
    --band: #0b0b0b;
    --brand: #d6ad57;
  }
  html, body {
    margin: 0;
    width: 1200px;
    height: 800px;
    overflow: hidden;
    background: var(--bg);
  }
  .canvas {
    position: relative;
    width: 1200px;
    height: 800px;
    font-family: "Roboto Condensed", "Arial Narrow", sans-serif;
  }
  .card {
    position: absolute;
    left: 100px;
    top: 95px;
    width: 1000px;
    height: 610px;
    background: var(--gold);
    overflow: hidden;
    box-shadow: 0 12px 30px rgba(0,0,0,0.25);
  }
  .card__art {
    position: absolute;
    inset: 0;
    width: 1000px;
    height: 610px;
  }
  .details {
    position: absolute;
    left: 70px;
    top: 60px;
    color: var(--ink);
  }
  .details__name {
    margin: 0;
    font-size: 52px;
    font-weight: 700;
    line-height: 1;
  }
  .details__title {
    margin: 8px 0 0;
    font-size: 32px;
    font-weight: 700;
    color: var(--accent-red);
  }
  .contact {
    list-style: none;
    margin: 48px 0 0;
    padding: 0;
    font-size: 22px;
    font-weight: 700;
  }
  .contact li {
    display: flex;
    align-items: center;
    gap: 10px;
    margin-bottom: 8px;
  }
  .contact svg { width: 22px; height: 22px; }
  .registration {
    position: absolute;
    left: 70px;
    top: 390px;
    width: 290px;
    color: var(--ink);
  }
  .registration__web {
    margin: 0;
    padding-bottom: 8px;
    font-size: 23px;
    font-weight: 700;
    border-bottom: 2px solid var(--ink);
  }
  .registration__line {
    margin: 6px 0 0;
    font-size: 20px;
    color: var(--accent-red);
  }
  .brand {
    position: absolute;
    left: 580px;
    top: 250px;
    width: 380px;
    text-align: center;
    font-size: 60px;
    font-weight: 700;
    line-height: 1.05;
    color: var(--brand);
    text-transform: uppercase;
  }
</style>
</head>
<body>
<main class="canvas">
  <section class="card">
    <svg class="card__art" viewBox="0 0 1000 610">
      <defs>
        <radialGradient id="scene-tone" cx="0.55" cy="0.45" r="0.65">
          <stop offset="0" stop-color="#a8432c"/>
          <stop offset="0.45" stop-color="#6a2a1b"/>
          <stop offset="1" stop-color="#120807"/>
        </radialGradient>
      </defs>
      <path d="M620 0 C490 80 420 270 410 610 L1000 610 L1000 0 Z" fill="var(--band)"/>
      <path d="M670 0 C540 80 465 270 455 610 L1000 610 L1000 0 Z" fill="var(--gold)"/>
      <path d="M682 0 C553 82 478 272 468 610 L1000 610 L1000 0 Z" fill="url(#scene-tone)" role="img" aria-label="Photo of a lit red brick wall above a timber floor"/>
    </svg>

    <div class="details">
      <h1 class="details__name">Your Name here</h1>
      <p class="details__title">Title here</p>
      <ul class="contact">
        <li>
          <svg viewBox="0 0 24 24"><path d="M6.6 10.8a15 15 0 0 0 6.6 6.6l2.2-2.2a1 1 0 0 1 1-.25 11.4 11.4 0 0 0 3.6.6 1 1 0 0 1 1 1V20a1 1 0 0 1-1 1A17 17 0 0 1 3 4a1 1 0 0 1 1-1h3.5a1 1 0 0 1 1 1c0 1.25.2 2.45.6 3.6a1 1 0 0 1-.25 1z" fill="var(--ink)"/></svg>
          0100-2200-4455
        </li>
        <li>
          <svg viewBox="0 0 24 24"><rect x="2" y="5" width="20" height="14" fill="var(--ink)"/><path d="M3 6l9 7 9-7" stroke="var(--gold)" stroke-width="2" fill="none"/></svg>
          youremailaddress@mail.com
        </li>
      </ul>
    </div>

    <div class="registration">
      <p class="registration__web">www.yourwebsite.com</p>
      <p class="registration__line">Licence Number : 1200456</p>
      <p class="registration__line">Abn : 120045678</p>
    </div>

    <p class="brand">Ridgeline<br>Builders</p>
  </section>
</main>
</body>
</html>
```